Letterhead for invoices and engagement letter

Want to use logos sourced on pixelbazaar to create letterhead templates for word or pdf files

Industry/Entity Type

Legal- law firm

Colors
0054AA
0677BA
7BADD7
CADEEF
E8F1F8

```html
<!DOCTYPE html>
<html lang="en">
<head>
<meta charset="utf-8">
<title>The Halden Firm – Letterhead</title>
<link rel="stylesheet" href="https://fonts.googleapis.com/css2?family=Lato:wght@400;700&display=swap">
<style>
  :root {
    --navy: #0d2039;
    --paper: #ffffff;
    --backdrop: #e4e5e7;
    --ink: #1c1c1c;
    --faint: #eef0f3;
  }
  * { margin: 0; padding: 0; box-sizing: border-box; }
  html, body {
    width: 1200px; height: 960px; overflow: hidden;
    background: var(--backdrop);
    font-family: "Lato", Arial, sans-serif;
  }
  .letterhead {
    position: absolute; left: 282px; top: 30px;
    width: 636px; height: 900px;
    background: var(--paper);
    box-shadow: 0 6px 24px rgba(0,0,0,.18);
    overflow: hidden;
  }
  .header-band { position: absolute; left: 0; top: 0; width: 636px; height: 260px; }
  .backdrop-ring { position: absolute; left: 250px; top: 250px; width: 300px; height: 300px; }
  .contact {
    position: absolute; right: 34px; top: 20px;
    color: #fff; font-size: 10.5px; line-height: 1.5;
    white-space: nowrap;
  }
  .contact .address { margin-bottom: 4px; }
  .contact li { list-style: none; display: flex; align-items: center; gap: 6px; }
  .contact svg { width: 9px; height: 9px; fill: #fff; flex: none; }
  .brand-mark {
    position: absolute; left: 36px; top: 158px;
    width: 92px; height: 92px; border-radius: 50%;
    background: var(--navy); border: 5px solid #fff;
    box-shadow: 0 0 0 3px var(--navy);
  }
  .brand-name {
    position: absolute; left: 40px; top: 266px;
    color: var(--navy); font-weight: 400; font-size: 22px;
    letter-spacing: 3px; text-transform: uppercase; line-height: 1.1;
  }
  .letter {
    position: absolute; left: 58px; top: 330px; right: 60px;
    color: var(--ink); font-size: 12px; line-height: 1.45;
  }
  .letter .date { margin-bottom: 14px; }
  .letter .recipient { margin-bottom: 14px; }
  .letter .address-block { margin-bottom: 22px; }
  .letter .salutation { color: var(--navy); font-weight: 700; font-size: 16px; margin-bottom: 14px; }
  .letter p.body { margin-bottom: 14px; }
  .letter .closing { margin-top: 14px; }
</style>
</head>
<body>
<main class="letterhead">
  <svg class="header-band" viewBox="0 0 636 260" aria-hidden="true">
    <path d="M0 0 H636 V150 C560 185 440 195 320 205 C230 213 140 215 0 228 Z" fill="var(--navy)"/>
    <path d="M636 122 C560 165 430 182 300 195 C220 203 150 207 90 210" fill="none" stroke="#fff" stroke-width="3"/>
    <path d="M636 140 C580 172 490 186 400 194" fill="none" stroke="#fff" stroke-width="1.5"/>
  </svg>

  <svg class="backdrop-ring" viewBox="0 0 300 300" aria-hidden="true">
    <circle cx="150" cy="150" r="140" fill="none" stroke="var(--faint)" stroke-width="10"/>
  </svg>

  <div class="contact">
    <div class="address">Your address, City<br>State, Zip 1234</div>
    <ul>
      <li><svg viewBox="0 0 10 10"><path d="M2 1 L4 1 L4.6 3 L3.5 4 C4 5.2 4.8 6 6 6.5 L7 5.4 L9 6 L9 8 C5 8.5 1.5 5 2 1 Z"/></svg>123 456 789</li>
      <li><svg viewBox="0 0 10 10"><path d="M1 2 H9 V8 H1 Z M1 2 L5 5.5 L9 2" fill="none" stroke="#fff" stroke-width="1"/></svg>info@yourmail.com</li>
      <li><svg viewBox="0 0 10 10"><circle cx="5" cy="5" r="4"/></svg>www.yourwebsite.com</li>
    </ul>
  </div>

  <div class="brand-mark" aria-hidden="true"></div>
  <div class="brand-name">The Halden Firm PLC</div>

  <section class="letter">
    <div class="date">January-03-2020</div>
    <div class="recipient">Mr, John Doe<br>President</div>
    <div class="address-block">Larkspur Corporation<br>123 Street Name, Suite# 10<br>City, State, 120023</div>
    <div class="salutation">Dear Mr, John</div>
    <p class="body">Lorem ipsum dolor sit amet, consectetur adipiscing elit, sed do eiusmod tempor incididunt ut labore et dolore magna aliqua. Ut enim ad minim veniam, quis nostrud exercitation ullamco laboris nisi ut aliquip ex ea commodo consequat. Duis aute irure dolor in reprehenderit in voluptate velit esse cillum dolore eu fugiat nulla pariatur.</p>
    <p class="body">Lorem ipsum dolor sit amet, consectetur adipiscing elit, sed do eiusmod tempor incididunt ut labore et dolore magna aliqua. Ut enim ad minim veniam, quis nostrud exercitation ullamco laboris nisi ut aliquip ex ea commodo consequat. Duis aute irure dolor in reprehenderit in voluptate velit esse cillum dolore eu fugiat nulla pariatur.</p>
    <p class="body">Lorem ipsum dolor sit amet, consectetur adipiscing elit, sed do eiusmod tempor incididunt ut labore et dolore magna aliqua. Ut enim ad minim veniam, quis nostrud exercitation ullamco laboris nisi ut aliquip ex ea commodo consequat.</p>
    <p class="body">Excepteur sint occaecat cupidatat non proident, sunt in culpa qui officia deserunt mollit anim id est laborum. re et dolore magnam aliquam quaerat voluptatem.</p>
    <div class="closing">Regards</div>
  </section>
</main>
</body>
</html>
```